KELO Produktdesign für goldene Collagen Eye Mask
Zielgruppe
Unsere Firma verkauf Luxus Kosmetik.
Aufgabenstellung
Wir suchen ein gutes Produktdesign für die Außenverpackung, die aufklappbar ist und die Innenverpackung für die goldenen Collagen Augenmasken. Das Design sollte in schwarz gold sein. Das KELO Logo sollte oben auf der Schachtel in Gold gut sichtbar sein. Am besten wäre eine goldene Erhebung des Logos. Wenn man die Schachtel aufklappt sollte innen noch ein schönes Foto zu erkennen sein. Z.b etwas das mit Blattgold oder Gold zu tun hat. Die Beschreibung sollte in deutsch und englisch auf die Verpackung. Ich lade hier Fotos von der alten Verpackung hoch, wo alle Informationen über das Produkt in englisch drauf stehen.
Das Produkt an sich sind Augenmasken mit Blattgold die Hyaluronsäure und Collagen beinhalten. In jeder Verpackung sollen 20 Stück sein.
Vorne auf der Verpackung wäre es schön, wenn dort VELORA DERM GOLD COLLAGEN Augenmaske stehen würde.
Hier ein Moodboard: Dieses Gefühl der Bilder beim betrachten sollte sich auf das Produktdesign anpassen.
https://brettwolke.co/m/7f41a9c2bd0e3356eacd102b88e4fa91

```html
<!DOCTYPE html>
<html lang="de">
<head>
<meta charset="utf-8">
<title>KELO – Verpackung innen</title>
<link rel="stylesheet" href="https://fonts.googleapis.com/css2?family=Archivo+Narrow:wght@400&family=Josefin+Sans:wght@300&display=swap">
<style>
  :root {
    --page: #ffffff;
    --ink: #1a1a1a;
    --black: #0b0b0b;
    --charcoal: #2a2a2a;
    --grey: #8a8a8a;
    --gold: #c9a24a;
    --gold-light: #e6c879;
    --gold-deep: #8a6a22;
  }
  * { margin: 0; padding: 0; box-sizing: border-box; }
  html, body {
    width: 1200px;
    height: 848px;
    overflow: hidden;
    background: var(--page);
  }
  .sheet {
    position: relative;
    width: 1200px;
    height: 848px;
  }
  .sheet-title {
    position: absolute;
    left: 100px;
    top: 60px;
    font-family: "Archivo Narrow", "Arial Narrow", sans-serif;
    font-weight: 400;
    font-size: 33px;
    letter-spacing: 0.2px;
    color: var(--ink);
  }
  .lid-insert {
    position: absolute;
    left: 363px;
    top: 228px;
    width: 473px;
    height: 452px;
    overflow: hidden;
    background: var(--black);
  }
  .lid-photo {
    position: absolute;
    inset: 0;
    background:
      radial-gradient(ellipse 45% 40% at 78% 30%, var(--gold-light) 0%, var(--gold) 30%, rgba(138,106,34,0.6) 55%, rgba(0,0,0,0) 80%),
      radial-gradient(ellipse 35% 30% at 85% 80%, #9c9c9c 0%, #4a4a4a 45%, rgba(0,0,0,0) 85%),
      linear-gradient(100deg, var(--black) 0%, var(--charcoal) 35%, #3a3a3a 55%, #1c1c1c 70%, #555 100%);
  }
  .brand {
    position: absolute;
    left: 33px;
    top: 343px;
    width: 150px;
  }
  .brand-name {
    font-family: "Josefin Sans", "Helvetica Neue", sans-serif;
    font-weight: 300;
    font-size: 62px;
    line-height: 1;
    letter-spacing: 4px;
    color: var(--gold);
  }
  .brand-rule {
    height: 1px;
    width: 146px;
    margin-top: 4px;
    background: var(--gold);
  }
  .brand-tagline {
    margin-top: 4px;
    font-family: "Josefin Sans", "Helvetica Neue", sans-serif;
    font-weight: 300;
    font-size: 11px;
    letter-spacing: 0.6px;
    color: var(--gold);
    white-space: nowrap;
  }
</style>
</head>
<body>
  <main class="sheet">
    <h1 class="sheet-title">VERPACKUNG INNEN (Deckel Unterseite oder Einleger)</h1>

    <section class="lid-insert">
      <div class="lid-photo" role="img" aria-label="Schwarz-weiß Foto einer Frau mit goldener venezianischer Maske, goldenen Bändern und schwarzen Federn"></div>

      <div class="brand">
        <div class="brand-name">KELO</div>
        <div class="brand-rule"></div>
        <div class="brand-tagline">the best beauty for you</div>
      </div>
    </section>
  </main>
</body>
</html>
```